New Physiotherapy Practice Website for an Award winning, Experienced Physio

Wanting to relaunch a 1 person physio practice. This is my academic CV
https://staffpages.tarrowvale.edu.example/en/people/dorian-keswick.
I want a simple, clear website that emphases My Name, My Experience, My Expertise, Location with a map, and Phone number (+ link to an online booking platform)
There aren't many clinicians around who also research and teach. I am unique with the awards I have won in each domain. I care about my patients, I listen, I am evidence based in my approach, I work WITH my clients I don't work AT my clients. I have experience with very acute through to chronic conditions, I have a range of expertise that set me apart in terms of advanced practice, hands- on technique and exercise based interventions. I am happy treating all musculoskeletal conditions but have a particular expertise in lower limb diagnosis and rehab and in providing second opinions. We have a large gym, medical, imaging, pharmacy in the same building. Easy parking and free for patients. Early morning bookings (0800) available but limited.
Facility is at https://www.tarrowvale.edu.example/health-clinics/contact-us
Target Market(s)
Local community needing injury diagnosis and treatment. Looking for skilled and experienced physio. "Hands of Experience"
Industry/Entity Type
Health (Physiotherapy)
Coding
Coded - Design and coding required
Number of Pages Required
1 page
Requirements
Must have
- Online booking button and phone number
Should not have
- Not too much focus on my research

```html
<!DOCTYPE html>
<html lang="en">
<head>
<meta charset="utf-8">
<title>Dr Dorian Keswick – Sports Physiotherapist</title>
<link rel="stylesheet" href="https://fonts.googleapis.com/css2?family=Montserrat:wght@400;500;600;700&display=swap">
<style>
:root{
  --blue:#2ba6de;
  --blue-dark:#1f8fc4;
  --ink:#222428;
  --body:#4a4d52;
  --muted:#6d7177;
  --line:#e3e6ea;
  --pale:#f1f5f8;
  --footer:#252627;
  --white:#ffffff;
}
*{box-sizing:border-box;margin:0;padding:0}
html,body{width:1200px;height:3603px;overflow:hidden}
body{font-family:'Montserrat',sans-serif;color:var(--ink);background:var(--white);position:relative}
a{color:inherit;text-decoration:none}
.abs{position:absolute}

/* header */
.site-header{position:absolute;top:0;left:0;width:1200px;height:109px;background:var(--white)}
.brand{left:109px;top:38px;font-size:26px;font-weight:700;letter-spacing:.2px}
.call{right:110px;top:20px;font-size:17px;font-weight:500;display:flex;align-items:center;gap:8px}
.main-nav{right:110px;top:66px;display:flex;gap:30px;font-size:17px;font-weight:500}
.main-nav .active{color:var(--blue)}

/* hero */
.hero{position:absolute;top:109px;left:0;width:1200px;height:619px;overflow:hidden}
.hero-bg{position:absolute;inset:0;background:linear-gradient(180deg,#5d6770 0%,#7c7670 45%,#9a8a78 75%,#8a7c6c 100%)}
.hero-shape{position:absolute;inset:0}
.portrait{position:absolute;left:612px;top:30px;width:530px;height:589px;border-radius:260px 260px 0 0;background:linear-gradient(180deg,#9aa7b3 0%,#6f8fb6 45%,#4f78ab 100%)}
.hero-copy{position:absolute;left:109px;top:160px;color:var(--white)}
.hero-copy h1{font-size:44px;font-weight:700;letter-spacing:.3px}
.hero-copy .role{font-size:27px;font-weight:600;margin-top:18px}
.hero-copy .title{font-size:17px;font-weight:500;line-height:31px;width:420px;margin-top:22px;padding-left:3px}
.btn{display:inline-flex;align-items:center;justify-content:center;border-radius:40px;font-weight:500;letter-spacing:.2px}
.btn-light{background:var(--white);color:var(--ink);width:198px;height:63px;font-size:20px;margin-top:26px;margin-left:3px}
.btn-blue{background:var(--blue);color:var(--white);width:198px;height:64px;font-size:20px}

/* feature strip */
.features{position:absolute;top:728px;left:0;width:1200px;height:133px;border-bottom:1px solid var(--line)}
.feature{position:absolute;top:28px;display:flex;align-items:center;gap:20px;font-size:20px;font-weight:500;line-height:31px}

/* experience */
.experience{position:absolute;top:861px;left:0;width:1200px;height:609px}
.section-title{font-size:38px;font-weight:700;letter-spacing:.3px}
.experience .section-title{position:absolute;left:109px;top:54px}
.exp-copy{position:absolute;left:112px;top:122px;width:490px;font-size:15.5px;line-height:27px;color:var(--body)}
.exp-copy p+p{margin-top:26px}
.pillar{position:absolute;left:647px;display:flex;gap:20px}
.pillar-icon{width:144px;height:144px;border:1.5px solid #a8adb3;border-radius:50%;display:flex;align-items:center;justify-content:center;flex:none}
.pillar h3{font-size:23px;font-weight:500;margin-top:16px}
.pillar p{font-size:15.5px;line-height:27px;color:var(--muted);margin-top:12px;width:300px}

/* services */
.services{position:absolute;top:1470px;left:0;width:1200px;height:766px;background:var(--pale)}
.centered{position:absolute;left:0;width:1200px;text-align:center}
.services .section-title{top:66px}
.service{position:absolute;top:154px;width:330px;text-align:center}
.service-photo{width:315px;height:315px;border-radius:50%;margin:0 auto}
.service-photo.selected{border:5px solid var(--blue)}
.service h3{font-size:24px;font-weight:500;line-height:29px;margin-top:24px}
.service p{font-size:16px;line-height:24px;color:var(--muted);margin-top:12px}
.arrow{position:absolute;top:300px}
.services .btn-blue{position:absolute;left:502px;top:627px}

/* facility */
.facility{position:absolute;top:2236px;left:0;width:1200px;height:522px}
.facility .section-title{top:60px}
.facility-grid{position:absolute;left:112px;top:145px;display:flex;gap:10px}
.facility-item{width:238px;text-align:center}
.facility-photo{width:238px;height:259px}
.facility-item h3{font-size:22px;font-weight:500;margin-top:22px}

/* contact */
.contact{position:absolute;top:2758px;left:0;width:1200px;height:576px;background:var(--pale)}
.contact .section-title{top:54px}
.map{position:absolute;left:112px;top:140px;width:563px;height:354px;background:linear-gradient(180deg,#a9d3a0 0%,#b9d9a8 38%,#7ea6e6 55%,#7aa3e6 100%)}
.contact-info{position:absolute;left:738px;top:185px}
.contact-info h3{font-size:22px;font-weight:500}
.contact-line{display:flex;gap:10px;font-size:15.5px;color:var(--body);margin-top:32px;line-height:28px}
.contact-line svg{margin-top:6px;flex:none}

/* footer */
.site-footer{position:absolute;top:3334px;left:0;width:1200px;height:269px;background:var(--footer);color:var(--white)}
.socials{position:absolute;top:47px;left:0;width:1200px;display:flex;justify-content:center;gap:6px}
.social{width:48px;height:48px;border-radius:50%;background:var(--white);display:flex;align-items:center;justify-content:center}
.footer-name{top:130px;font-size:28px;font-weight:700}
.footer-nav{top:186px;display:flex;justify-content:center;gap:30px;font-size:18px;font-weight:500}
.copyright{top:230px;font-size:16px;color:#e6e6e6}
</style>
</head>
<body>

<header class="site-header">
  <div class="abs brand">DR DORIAN KESWICK</div>
  <div class="abs call">
    <svg width="16" height="16" viewBox="0 0 24 24"><path fill="#2ba6de" d="M6.6 10.8a15.2 15.2 0 0 0 6.6 6.6l2.2-2.2c.3-.3.7-.4 1-.2 1.1.4 2.3.6 3.6.6.6 0 1 .4 1 1V20c0 .6-.4 1-1 1A17 17 0 0 1 3 4c0-.6.4-1 1-1h3.5c.6 0 1 .4 1 1 0 1.3.2 2.5.6 3.6.1.3 0 .7-.2 1z"/></svg>
    <span>CALL: 1 555 010 2040</span>
  </div>
  <nav class="abs main-nav">
    <a class="active" href="#">Home</a><a href="#">About</a><a href="#">Services</a><a href="#">Facilities</a><a href="#">Contact Us</a>
  </nav>
</header>

<section class="hero">
  <div class="hero-bg" role="img" aria-label="Softly blurred clinic interior"></div>
  <svg class="hero-shape" width="1200" height="619" viewBox="0 0 1200 619">
    <polygon points="757,0 1200,0 1200,619 517,619" fill="#2ba6de" opacity=".92"/>
    <polygon points="1130,0 1200,0 1200,619 1160,619" fill="#7fb7d8" opacity=".6"/>
  </svg>
  <div class="portrait" role="img" aria-label="Portrait of Dr Dorian Keswick in a blue shirt"></div>
  <div class="hero-copy">
    <h1>DR DORIAN KESWICK (PHD)</h1>
    <div class="role">Sports Physiotherapist</div>
    <p class="title">Titled Member of the Southland College of Physiotherapists</p>
    <a class="btn btn-light" href="#">BOOK ONLINE</a>
  </div>
</section>

<section class="features">
  <div class="feature" style="left:133px">
    <svg width="60" height="80" viewBox="0 0 60 80"><path d="M30 2C14 2 2 14 2 30c0 20 28 48 28 48s28-28 28-48C58 14 46 2 30 2z" fill="#2ba6de"/><circle cx="30" cy="29" r="17" fill="none" stroke="#fff" stroke-width="3"/><path d="M25 39V20h7a5.5 5.5 0 0 1 0 11h-7" fill="none" stroke="#fff" stroke-width="3.5"/></svg>
    <span>Easy and free<br>parking</span>
  </div>
  <div class="feature" style="left:430px">
    <svg width="78" height="78" viewBox="0 0 78 78"><rect x="3" y="10" width="58" height="52" rx="4" fill="none" stroke="#2ba6de" stroke-width="4"/><rect x="3" y="10" width="58" height="12" fill="#2ba6de"/><rect x="14" y="3" width="5" height="14" rx="2" fill="#2ba6de"/><rect x="45" y="3" width="5" height="14" rx="2" fill="#2ba6de"/><g fill="#2ba6de"><rect x="11" y="29" width="8" height="7"/><rect x="23" y="29" width="8" height="7"/><rect x="35" y="29" width="8" height="7"/><rect x="11" y="41" width="8" height="7"/><rect x="23" y="41" width="8" height="7"/><rect x="11" y="52" width="8" height="6"/></g><circle cx="58" cy="58" r="17" fill="#fff" stroke="#2ba6de" stroke-width="4"/><path d="M58 48v11h8" fill="none" stroke="#2ba6de" stroke-width="4"/></svg>
    <span>Early morning bookings<br>available but limited</span>
  </div>
  <div class="feature" style="left:830px">
    <svg width="72" height="72" viewBox="0 0 72 72"><circle cx="32" cy="9" r="7" fill="#2ba6de"/><path d="M24 20h16l6 16H36l-4-8-6 12H18z" fill="#2ba6de"/><circle cx="12" cy="44" r="6" fill="#2ba6de"/><rect x="18" y="40" width="46" height="10" rx="4" fill="#2ba6de"/><rect x="2" y="54" width="68" height="6" fill="#2ba6de"/><rect x="6" y="60" width="5" height="10" fill="#2ba6de"/><rect x="61" y="60" width="5" height="10" fill="#2ba6de"/></svg>
    <span>Experienced<br>Physiotherapist</span>
  </div>
</section>

<section class="experience">
  <h2 class="section-title">HANDS OF EXPERIENCE</h2>
  <div class="exp-copy">
    <p>If you are looking for depth of knowledge, a treatment alternative, or a second opinion for your pain or injury then Dorian has more than 30 years of clinical experience - applying the best of communication , empathy, evidence and skill.</p>
    <p>Dorian is an expert in his field. He has 9 excellence awards on top of his 3 degrees.</p>
    <p>He currently teaches Physiotherapy to the next generation of clinicians, and mentors and supervises qualified clinicians.</p>
    <p>Dorian has worked in roles in Emergency and Elite sports to an International level. He has worked for 20 years with military from general services to elite forces, managing all range of injuries, from head to toe.</p>
  </div>
  <div class="pillar" style="top:82px">
    <div class="pillar-icon">
      <svg width="92" height="84" viewBox="0 0 92 84" fill="none" stroke="#2ba6de" stroke-width="3"><circle cx="46" cy="12" r="9"/><path d="M32 50V34a14 14 0 0 1 28 0v16"/><path d="M16 58l4 8h8l-6 5 2 8-8-5-8 5 2-8-6-5h8z"/><path d="M46 52l4 9h9l-7 6 3 9-9-6-9 6 3-9-7-6h9z"/><path d="M76 58l4 8h8l-6 5 2 8-8-5-8 5 2-8-6-5h8z"/></svg>
    </div>
    <div><h3>Experience</h3><p>I have experience with very acute through to chronic conditions</p></div>
  </div>
  <div class="pillar" style="top:255px">
    <div class="pillar-icon">
      <svg width="90" height="90" viewBox="0 0 90 90" fill="none" stroke="#2ba6de" stroke-width="3"><path d="M30 84V68c-10-6-16-16-16-28a30 30 0 0 1 60 0l6 14h-7v12H60v18"/><circle cx="36" cy="36" r="9"/><path d="M36 18v6M36 48v6M18 36h6M48 36h6M24 24l4 4M44 44l4 4M24 48l4-4M44 28l4-4"/></svg>
    </div>
    <div><h3>Expertise</h3><p>I have a range of expertise that set me apart in terms of advanced practice, hands- on technique and exercise based interventions.</p></div>
  </div>
</section>

<section class="services">
  <h2 class="section-title centered">IF YOU NEED</h2>
  <svg class="arrow" style="left:46px" width="20" height="32" viewBox="0 0 20 32"><path d="M15 4L4 16l11 12" fill="none" stroke="#444" stroke-width="3"/></svg>
  <svg class="arrow" style="left:1134px" width="20" height="32" viewBox="0 0 20 32"><path d="M5 4l11 12L5 28" fill="none" stroke="#444" stroke-width="3"/></svg>
  <div class="service" style="left:104px">
    <div class="service-photo selected" role="img" aria-label="Physiotherapist examining a patient's knee" style="background:linear-gradient(135deg,#e9c2a4 0%,#d49a78 45%,#3b7fb8 100%)"></div>
    <h3>Acute Sports Injury<br>management</h3>
    <p>Ankle, Foot, Knee, Hip, Shins,<br>Shoulder, Hand</p>
  </div>
  <div class="service" style="left:436px">
    <div class="service-photo" role="img" aria-label="Therapist assisting a patient's shoulder stretch" style="background:linear-gradient(160deg,#cfdbe6 0%,#a77e67 45%,#2ba6de 100%)"></div>
    <h3>Back or Neck<br>therapy</h3>
  </div>
  <div class="service" style="left:767px">
    <div class="service-photo" role="img" aria-label="Patient in a knee brace exercising on a ball" style="background:linear-gradient(135deg,#4a3e36 0%,#6b5a4c 40%,#3f9fd8 75%,#e7ecef 100%)"></div>
    <h3>Rehab after surgery or<br>Advice and pre-hab<br>before surgery</h3>
  </div>
  <a class="btn btn-blue" href="#">BOOK ONLINE</a>
</section>

<section class="facility">
  <h2 class="section-title centered">FACILITY</h2>
  <div class="facility-grid">
    <div class="facility-item"><div class="facility-photo" role="img" aria-label="Large gym with exercise equipment" style="background:linear-gradient(180deg,#e6e9ec 0%,#b7bcc2 50%,#8f8a86 100%)"></div><h3>Large gym</h3></div>
    <div class="facility-item"><div class="facility-photo" role="img" aria-label="Patient walking on a treadmill" style="background:linear-gradient(180deg,#6d7986 0%,#b9c0c7 50%,#e4e6e9 100%)"></div><h3>Medical</h3></div>
    <div class="facility-item"><div class="facility-photo" role="img" aria-label="Patient in an imaging scanner" style="background:linear-gradient(160deg,#f3e1b5 0%,#e8c46b 35%,#c9d6e6 70%,#f2ece4 100%)"></div><h3>Imaging</h3></div>
    <div class="facility-item"><div class="facility-photo" role="img" aria-label="Patient with a walker in a pharmacy aisle" style="background:linear-gradient(90deg,#e7e9ec 0%,#c7ccd2 40%,#5b6675 60%,#e4e1de 100%)"></div><h3>Pharmacy</h3></div>
  </div>
</section>

<section class="contact">
  <h2 class="section-title centered">CONTACT</h2>
  <div class="map" role="img" aria-label="Map of the clinic location and surrounding coast"></div>
  <div class="contact-info">
    <h3>Contact Information</h3>
    <div class="contact-line"><svg width="14" height="14" viewBox="0 0 24 24"><path fill="#2ba6de" d="M6.6 10.8a15.2 15.2 0 0 0 6.6 6.6l2.2-2.2c.3-.3.7-.4 1-.2 1.1.4 2.3.6 3.6.6.6 0 1 .4 1 1V20c0 .6-.4 1-1 1A17 17 0 0 1 3 4c0-.6.4-1 1-1h3.5c.6 0 1 .4 1 1 0 1.3.2 2.5.6 3.6.1.3 0 .7-.2 1z"/></svg><span>1 555 010 2040</span></div>
    <div class="contact-line"><svg width="17" height="13" viewBox="0 0 17 13"><rect width="17" height="13" rx="1.5" fill="#2ba6de"/><path d="M1 1.5l7.5 6 7.5-6" fill="none" stroke="#fff" stroke-width="1.4"/></svg><span>info@doriankeswick.example</span></div>
    <div class="contact-line"><svg width="12" height="16" viewBox="0 0 12 16"><path d="M6 0a6 6 0 0 0-6 6c0 4.5 6 10 6 10s6-5.5 6-10a6 6 0 0 0-6-6z" fill="#2ba6de"/><circle cx="6" cy="6" r="2.2" fill="#fff"/></svg><span>12345 Duis aute irure dolor . Suite 117<br>&nbsp;Tarrowvale, VA 20990</span></div>
  </div>
</section>

<footer class="site-footer">
  <div class="socials">
    <a class="social" href="#" aria-label="Social profile"></a>
    <a class="social" href="#" aria-label="Social profile"></a>
    <a class="social" href="#" aria-label="Social profile"></a>
    <a class="social" href="#" aria-label="Email"><svg width="22" height="16" viewBox="0 0 22 16"><rect width="22" height="16" rx="2" fill="#2ba6de"/><path d="M1 2l10 7 10-7" fill="none" stroke="#fff" stroke-width="1.8"/></svg></a>
  </div>
  <div class="abs centered footer-name">DR DORIAN KESWICK</div>
  <nav class="abs centered footer-nav"><a href="#">HOME</a><a href="#">ABOUT</a><a href="#">SERVICES</a><a href="#">FACILITIES</a><a href="#">CONTACT US</a></nav>
  <div class="abs centered copyright">Copyright © 2022, Dorian Keswick. All rights reserved.</div>
</footer>

</body>
</html>
```